Motor Vehicle Wholesale Business Card design

I will be buying and selling cars throughout the motor car industry. I will be purchasing cars from one yard and wholesaling these cars to other motor car retailers. I am open to designs. I would think a car would be required within the logo, and generally the cars are mainstream cars. Please do not use prestige cars in the logo.If not a car in the logo, then i am open to designs that do also indicate this as well.

This is not a retail business, just wholesale only.

Thanks

Target Market(s)

car dealers/dealerships

Industry/Entity Type

Retail

Contact Information for Business Card

TRD Wholesale
Colin Hartwell
Mob: 0438207164

Requirements
Must have
• A picture of a car or a representation of a car is required as i am dealing in the motor vehicle industry.

```html
<!DOCTYPE html>
<html lang="en">
<head>
<meta charset="utf-8">
<title>TRD Wholesale – Business Card</title>
<link href="https://fonts.googleapis.com/css2?family=Arimo:wght@400;700&display=swap" rel="stylesheet">
<style>
  :root {
    --bg-top: #3c3d3e;
    --bg-light: #f4f4f4;
    --bg-mid: #8a8a8a;
    --bg-dark: #050505;
    --brand-red: #de1b22;
    --car-dark: #1c1c1c;
    --car-soft: #6a6a6a;
    --text-white: #ffffff;
  }
  html, body {
    margin: 0;
    padding: 0;
    width: 1200px;
    height: 741px;
    overflow: hidden;
    background: #000;
  }
  .card {
    position: relative;
    width: 1200px;
    height: 741px;
    overflow: hidden;
    font-family: "Arimo", Arial, sans-serif;
    color: var(--text-white);
    background: linear-gradient(
      to bottom,
      var(--bg-top) 0%,
      #9a9a9a 18%,
      var(--bg-light) 36%,
      #e2e2e2 44%,
      var(--bg-mid) 54%,
      #2a2a2a 64%,
      var(--bg-dark) 76%,
      var(--bg-dark) 100%
    );
  }
  .car-visual {
    position: absolute;
    left: 232px;
    top: 118px;
    width: 730px;
    height: 210px;
    border-radius: 50% 50% 12% 12% / 70% 70% 20% 20%;
    background: radial-gradient(ellipse at 50% 35%, var(--car-dark) 0%, var(--car-soft) 55%, rgba(106,106,106,0) 75%);
    opacity: 0.8;
  }
  .brand {
    position: absolute;
    left: 0;
    right: 0;
    top: 268px;
    margin: 0;
    text-align: center;
    font-weight: 700;
    font-size: 100px;
    letter-spacing: 2px;
    color: var(--brand-red);
    line-height: 1;
  }
  .brand-shadow {
    position: absolute;
    left: 230px;
    top: 452px;
    width: 742px;
    height: 22px;
  }
  .holder-name {
    position: absolute;
    left: 0;
    right: 0;
    top: 484px;
    margin: 0;
    text-align: center;
    font-size: 52px;
    font-weight: 400;
    line-height: 1;
  }
  .holder-name span {
    display: inline-block;
    padding-bottom: 4px;
    border-bottom: 3px solid var(--text-white);
  }
  .contact {
    position: absolute;
    display: grid;
    grid-template-columns: auto auto auto;
    column-gap: 8px;
    row-gap: 12px;
    align-items: baseline;
    line-height: 1.1;
  }
  .contact-left { left: 110px; top: 568px; }
  .contact-right { left: 775px; top: 572px; row-gap: 10px; }
  .contact .label {
    text-align: right;
    font-size: 36px;
  }
  .contact .sep { font-size: 34px; }
  .contact .value { font-size: 30px; }
  .contact-right .label, .contact-right .value { font-size: 36px; }
</style>
</head>
<body>
  <main class="card">
    <div class="car-visual" role="img" aria-label="Car silhouette illustration"></div>
    <h2 class="brand">TRD Wholesale</h2>
    <svg class="brand-shadow" viewBox="0 0 742 22" aria-hidden="true">
      <defs>
        <radialGradient id="floorShadow" cx="50%" cy="50%" r="50%">
          <stop offset="0%" stop-color="#2b2b2b" stop-opacity="0.9"/>
          <stop offset="100%" stop-color="#2b2b2b" stop-opacity="0"/>
        </radialGradient>
      </defs>
      <ellipse cx="371" cy="11" rx="371" ry="9" fill="url(#floorShadow)"/>
    </svg>

    <h1 class="holder-name"><span>Colin Hartwell</span></h1>

    <div class="contact contact-left">
      <span class="label">Mob</span><span class="sep">:</span><span class="value">( your mobile number )</span>
      <span class="label">Fax</span><span class="sep">:</span><span class="value">( your fax number )</span>
      <span class="label">Email</span><span class="sep">:</span><span class="value">( your email )</span>
    </div>

    <div class="contact contact-right">
      <span class="label">IMCT</span><span class="sep">:</span><span class="value">0000000</span>
      <span class="label">ABN</span><span class="sep">:</span><span class="value">0000000</span>
      <span class="label">ACN</span><span class="sep">:</span><span class="value">0000000</span>
    </div>
  </main>
</body>
</html>
```